Business Cards - New Logo Rebranding

Hello We know have a red and blue logo and are looking to create new cards. We are looking for the best creativity of the new logo merged with some of the existing artwork provided.

Target Market(s)

Realtors

Industry/Entity Type

Real Estate

Contact Information for Business Card

New logo with rebranded colors

Requirements
Must have
• Creative use of the new logo

```html
<!DOCTYPE html>
<html lang="en">
<head>
<meta charset="utf-8">
<title>Summit Crest Business Cards</title>
<link href="https://fonts.googleapis.com/css2?family=Open+Sans:wght@400;600;700;800&family=Oswald:wght@500;600&display=swap" rel="stylesheet">
<style>
  :root{
    --orange:#f29a1c;
    --gold:#f7c93a;
    --black:#000;
    --white:#fff;
    --ink:#111;
  }
  html,body{margin:0;padding:0;width:1200px;height:1200px;overflow:hidden;background:var(--black);}
  .canvas{position:relative;width:1200px;height:1200px;font-family:"Open Sans",sans-serif;}
  .card{position:absolute;overflow:hidden;background:var(--white);}
  .card svg.bg{position:absolute;left:0;top:0;}
  .abs{position:absolute;}
  .center{left:0;right:0;text-align:center;}

  /* front */
  .card-front{left:102px;top:201px;width:480px;height:798px;}
  .portrait{position:absolute;left:110px;top:45px;width:260px;height:290px;
    background:linear-gradient(180deg,#c9975f 0%,#3a5fb0 70%,#2c4fa0 100%);border-radius:120px 120px 0 0;opacity:.9;}
  .brand-name{top:394px;font-weight:800;font-size:41px;line-height:50px;letter-spacing:2px;color:var(--orange);white-space:nowrap;}
  .brand-tag{top:453px;left:68px;right:68px;display:flex;align-items:center;gap:6px;font-weight:700;font-size:12.5px;color:var(--ink);white-space:nowrap;}
  .brand-tag .rule{flex:1;height:2px;background:var(--ink);}
  .person-name{top:482px;font-weight:700;font-size:35px;line-height:44px;color:var(--ink);}
  .person-title{top:524px;font-weight:600;font-size:20px;line-height:26px;color:var(--orange);}
  .contact-icons{top:572px;display:flex;justify-content:center;gap:7px;}
  .contact-list{top:600px;font-size:20px;line-height:25px;color:var(--ink);}
  .contact-list .hl{color:var(--orange);font-weight:600;}
  .services{left:0;right:0;top:722px;height:76px;background:var(--black);color:var(--orange);
    font-family:"Oswald",sans-serif;font-weight:500;font-size:21px;text-align:center;padding-top:8px;box-sizing:border-box;letter-spacing:-.3px;white-space:nowrap;}

  /* back */
  .card-back{left:620px;top:203px;width:477px;height:795px;}
  .headline{top:48px;font-weight:700;font-size:26px;line-height:33px;color:var(--white);letter-spacing:.3px;}
  .why{top:156px;font-family:"Oswald",sans-serif;font-weight:600;font-size:31px;line-height:40px;color:var(--orange);letter-spacing:-.5px;white-space:nowrap;}
  .reasons{left:54px;top:210px;margin:0;padding:0;list-style:none;color:var(--orange);font-size:21px;line-height:25px;}
  .reasons li{position:relative;padding-left:32px;margin-bottom:15px;white-space:nowrap;}
  .reasons li::before{content:"";position:absolute;left:0;top:3px;width:22px;height:22px;border-radius:50%;background:var(--orange);box-shadow:inset 0 0 0 3px #fbd7a0;}
</style>
</head>
<body>
<div class="canvas">

  <section class="card card-front">
    <svg class="bg" width="480" height="798" viewBox="0 0 480 798">
      <defs>
        <linearGradient id="frontGlow" x1="0" y1="0" x2="1" y2="0">
          <stop offset="0" stop-color="#f29a1c"/>
          <stop offset="1" stop-color="#fbd59a"/>
        </linearGradient>
      </defs>
      <polygon points="0,0 480,0 480,300 240,352 0,300" fill="url(#frontGlow)"/>
      <circle cx="240" cy="200" r="210" fill="none" stroke="#fff" stroke-opacity=".15" stroke-width="14"/>
    </svg>
    <div class="portrait" role="img" aria-label="Portrait photo of the inspector in a blue polo shirt"></div>
    <svg class="bg" width="480" height="798" viewBox="0 0 480 798">
      <polygon points="0,300 240,352 480,300 480,306 240,360 0,306" fill="#000"/>
      <circle cx="240" cy="339" r="66" fill="#fff"/>
      <circle cx="240" cy="339" r="61" fill="#000"/>
    </svg>
    <div class="abs center brand-name">SUMMIT CREST</div>
    <div class="abs brand-tag"><span class="rule"></span>INSPECTION PROFESSIONALS<span class="rule"></span></div>
    <div class="abs center person-name">Dan Marlowe</div>
    <div class="abs center person-title">Certified Mold Inspector</div>
    <div class="abs center contact-icons">
      <svg width="24" height="24" viewBox="0 0 24 24"><circle cx="12" cy="12" r="12"/><path d="M8 6l2 3-1.5 1.5c1 2 2.5 3.5 4.5 4.5L14.5 13.5l3 2-1.5 2.5C11 17.5 6.5 13 6 7.5z" fill="#fff"/></svg>
      <svg width="24" height="24" viewBox="0 0 24 24"><circle cx="12" cy="12" r="12"/><rect x="8.5" y="5.5" width="7" height="13" rx="1.5" fill="none" stroke="#fff" stroke-width="1.6"/></svg>
      <svg width="24" height="24" viewBox="0 0 24 24"><circle cx="12" cy="12" r="12"/><rect x="6" y="8" width="12" height="8.5" fill="none" stroke="#fff" stroke-width="1.6"/><path d="M6 8l6 5 6-5" fill="none" stroke="#fff" stroke-width="1.6"/></svg>
      <svg width="24" height="24" viewBox="0 0 24 24"><circle cx="12" cy="12" r="12"/><g fill="none" stroke="#fff" stroke-width="1.4"><circle cx="12" cy="12" r="6.5"/><ellipse cx="12" cy="12" rx="3" ry="6.5"/><path d="M5.5 12h13"/></g></svg>
    </div>
    <div class="abs center contact-list">
      800.555.0142<br>
      562.555.0187<br>
      dan@summitcrestinspect.com<br>
      www.<span class="hl">SummitCrestInspect</span>.com
    </div>
    <div class="abs services">HOME · SEWER · MOLD · COMMERCIAL · TERMITE · ROOF</div>
  </section>

  <section class="card card-back">
    <svg class="bg" width="477" height="795" viewBox="0 0 477 795">
      <defs>
        <linearGradient id="backGlow" x1="0" y1="0" x2="1" y2="0">
          <stop offset="0" stop-color="#f29a1c"/>
          <stop offset="1" stop-color="#f7c93a"/>
        </linearGradient>
      </defs>
      <polygon points="0,0 477,0 477,99 239,151 0,101" fill="url(#backGlow)"/>
      <polygon points="0,585 239,622 477,585 477,795 0,795" fill="url(#backGlow)"/>
      <g role="img" aria-label="Certification and review badges">
        <circle cx="120" cy="626" r="41" fill="#b22234"/><circle cx="120" cy="626" r="33" fill="#2d3470"/>
        <circle cx="240" cy="626" r="41" fill="#c9a83c"/><circle cx="240" cy="626" r="33" fill="#3c4a5c"/>
        <circle cx="358" cy="626" r="41" fill="#c8c2a8"/><circle cx="358" cy="626" r="33" fill="#4a4a4a"/>
        <rect x="86" y="692" width="142" height="50" fill="#2d3470"/><circle cx="100" cy="717" r="30" fill="#6b7aa8"/>
        <rect x="240" y="680" width="96" height="64" rx="6" fill="#d32323"/>
        <circle cx="390" cy="710" r="24" fill="#fff" opacity=".85"/>
      </g>
    </svg>
    <div class="abs center headline">CALIFORNIA’S #1<br>INSPECTION COMPANY!</div>
    <div class="abs center why">WHY CHOOSE SUMMIT CREST...</div>
    <ul class="abs reasons">
      <li>Performing Inspections Since 1984</li>
      <li>NorthHome Certified Master<br>/ Professional Inspectors®</li>
      <li>500,000+ Inspections<br>Completed Statewide</li>
      <li>Request of Repairs Pricer Report</li>
      <li>90-Day Inspection Guarantees</li>
      <li>Federal Drone Licensed Roof<br>Inspectors upon request</li>
      <li>5,000+ 5-Star Reviews on<br>Searchly &amp; Ratewise</li>
    </ul>
  </section>

</div>
</body>
</html>
```